Design the Business card for VaultPeak

Business card required for a professional Cyber Security business.
Company Logo and Icon has already been provided however I would like other options for the logo and icon to compare to. Alternatively, please refine/enhance the image of the logo.icon I have already provided.

If you are going to use the provided logo and icon, I was thinking that the company raised Logo on White background would serve well on the front of the card. See attached. AND, a large company raised stand-alone icon to appear on black background on the back of the card with tagline 'Cyber Risk Management, Governance and Consulting' or 'Cyber Security for your Business' See attached.
Alternatively, provide your own design for the logo and icon.

Target Market(s)

Enterprise, Government, Financial.

Contact Information for Business Card

Teodor Halvik
Founder and CEO

Email Address
Mobile Number
Website URL
LinkedIn URL

Logo Text

VaultPeak - see attached example of logo

Font styles to use
Other font styles liked:
• Berlin Sans FB

Requirements
Must have
• Clean large and bold icon on the back with tagline.
• Horizontal alignment,
Nice to have
• Round edges.
• Raised Logo/Icon
Should not have
• An unprofessional look and feel.

```html
<!DOCTYPE html>
<html lang="en">
<head>
<meta charset="utf-8">
<title>VaultPeak Business Card</title>
<link rel="stylesheet" href="https://fonts.googleapis.com/css2?family=Roboto:wght@400;500;700&family=Roboto+Condensed:wght@500&family=Cabin:wght@500&display=swap">
<style>
  :root {
    --backdrop: #e9e5df;
    --card-white: #f4f4f4;
    --card-black: #1b1c1e;
    --brand-blue: #1a6fc0;
    --band-blue: #4a78c8;
    --accent-yellow: #f2b705;
    --text-grey: #4a4a4a;
    --divider: #b9b9b9;
    --ornament-tint: rgba(26, 111, 192, 0.16);
  }
  * { margin: 0; padding: 0; box-sizing: border-box; }
  html, body { width: 1200px; height: 960px; overflow: hidden; }
  body { background: var(--backdrop); position: relative; font-family: "Roboto", sans-serif; }

  .card {
    position: absolute;
    width: 600px;
    height: 343px;
    box-shadow: 0 3px 8px rgba(0,0,0,0.35);
  }
  .card-front { left: 314px; top: 113px; background: var(--card-white); }
  .card-back { left: 311px; top: 472px; background: var(--card-black); }

  .corner-ornament {
    position: absolute;
    width: 110px;
    height: 120px;
    background: var(--ornament-tint);
  }
  .corner-ornament-top { left: 8px; top: 0; border-bottom-right-radius: 100%; }
  .corner-ornament-bottom { right: 0; bottom: 0; border-top-left-radius: 100%; }

  .brand { position: absolute; display: flex; align-items: center; }
  .brand-mark { border-radius: 50%; background: var(--brand-blue); flex: none; }
  .brand-name {
    font-family: "Roboto", sans-serif;
    font-weight: 500;
    color: var(--brand-blue);
    letter-spacing: -0.5px;
    line-height: 1;
  }
  .card-front .brand { left: 122px; top: 62px; gap: 16px; }
  .card-front .brand-mark { width: 84px; height: 84px; }
  .card-front .brand-name { font-size: 60px; }

  .person { position: absolute; right: 318px; top: 196px; text-align: right; }
  .person-name {
    font-family: "Roboto Condensed", sans-serif;
    font-weight: 500;
    font-size: 22px;
    color: var(--brand-blue);
    line-height: 24px;
  }
  .person-title {
    font-family: "Roboto", sans-serif;
    font-weight: 500;
    font-size: 15px;
    color: var(--accent-yellow);
    line-height: 22px;
  }
  .divider {
    position: absolute; left: 300px; top: 177px;
    width: 1px; height: 80px; background: var(--divider);
  }
  .contact-list { position: absolute; left: 319px; top: 178px; list-style: none; }
  .contact-item {
    display: flex; align-items: center; gap: 9px;
    font-size: 14.5px; color: var(--text-grey); height: 19.3px;
  }
  .contact-icon { width: 13px; height: 13px; flex: none; }

  .card-back .brand { left: 125px; top: 116px; gap: 12px; }
  .card-back .brand-mark { width: 84px; height: 84px; }
  .card-back .brand-name { font-size: 56px; }

  .tagline-band {
    position: absolute; left: 0; top: 269px; width: 600px; height: 35px;
    background: var(--band-blue);
    display: flex; align-items: center; justify-content: center;
    font-family: "Cabin", sans-serif; font-weight: 500;
    font-size: 19.5px; color: #ffffff;
  }
</style>
</head>
<body>

<section class="card card-front">
  <div class="corner-ornament corner-ornament-top" role="img" aria-label="Decorative circuit arc ornament in the top-left corner"></div>
  <div class="corner-ornament corner-ornament-bottom" role="img" aria-label="Decorative circuit arc ornament in the bottom-right corner"></div>

  <div class="brand">
    <span class="brand-mark"></span>
    <span class="brand-name">VaultPeak</span>
  </div>

  <div class="person">
    <p class="person-name">TEODOR HALVIK</p>
    <p class="person-title">FOUNDER &amp; CEO</p>
  </div>

  <span class="divider"></span>

  <ul class="contact-list">
    <li class="contact-item">
      <svg class="contact-icon" viewBox="0 0 13 13"><rect x="3" y="0.5" width="7" height="12" rx="1.2" fill="none" stroke="var(--brand-blue)" stroke-width="1.6"/><circle cx="6.5" cy="10.3" r="0.9" fill="var(--brand-blue)"/></svg>
      555 014 2290
    </li>
    <li class="contact-item">
      <svg class="contact-icon" viewBox="0 0 13 13"><rect x="0.5" y="2.5" width="12" height="8" fill="var(--brand-blue)"/><path d="M0.5 2.5 L6.5 7 L12.5 2.5" fill="none" stroke="#ffffff" stroke-width="1"/></svg>
      teodor@vaultpeak.com
    </li>
    <li class="contact-item">
      <svg class="contact-icon" viewBox="0 0 13 13"><circle cx="6.5" cy="6.5" r="6" fill="var(--brand-blue)"/><path d="M3 4 Q5 3 6 5 Q7 7 5 8 M8 9 Q9 7 10.5 7.5" fill="none" stroke="#ffffff" stroke-width="1.2"/></svg>
      www.vaultpeak.com
    </li>
    <li class="contact-item">
      <svg class="contact-icon" viewBox="0 0 13 13"><circle cx="6.5" cy="6.5" r="6" fill="var(--brand-blue)"/><rect x="4" y="5.4" width="1.4" height="4" fill="#ffffff"/><rect x="6.6" y="5.4" width="2.8" height="4" fill="#ffffff"/></svg>
      vaultpeak
    </li>
  </ul>
</section>

<section class="card card-back">
  <div class="brand">
    <span class="brand-mark"></span>
    <span class="brand-name">VaultPeak</span>
  </div>
  <p class="tagline-band">Cyber Risk Management, Governance &amp; Consulting</p>
</section>

</body>
</html>
```